Computer tuition business needs Business card and Advertising Flyer

I am starting up a new business "Derek Halloway Computer Services" (DHCS for short) based in the Manning Valley NSW Australia.
The primary focus is on tuition\advice to the elderly and less computer literate in the region.
I will not be providing any repair services.

I have the line "At your home, On your computer, Answering your questions" in my head

I will need a Business card design (one sided) and Advertising Flyer design (A4 size, grayscale ).

Contact details on all these are - Mobile: 0412-583-906
- Email : dhalloway.pcservices@brindlemail.example

Target Market(s)

The primary focus is on tuition\advice to the elderly and less computer literate in the Manning Valley region of

Industry/Entity Type

Computer

```html
<!DOCTYPE html>
<html lang="en">
<head>
<meta charset="utf-8">
<title>Derek Halloway Computer Services – Flyer</title>
<link rel="stylesheet" href="https://fonts.googleapis.com/css2?family=Righteous&family=Open+Sans:wght@400;700&display=swap">
<style>
  :root {
    --backdrop: #e6e3df;
    --paper: #ffffff;
    --ink: #1f1d1e;
    --grey: #58585a;
    --band: #231f20;
    --band-text: #ffffff;
  }
  * { margin: 0; padding: 0; box-sizing: border-box; }
  html, body {
    width: 1200px;
    height: 750px;
    overflow: hidden;
    background: var(--backdrop);
  }
  .canvas {
    position: relative;
    width: 1200px;
    height: 750px;
  }
  .flyer {
    position: absolute;
    left: 353px;
    top: 27px;
    width: 494px;
    height: 696px;
    background: var(--paper);
    box-shadow: 0 4px 14px rgba(0,0,0,0.18);
  }
  .flyer__headline {
    position: absolute;
    top: 40px;
    left: 0;
    width: 100%;
    text-align: center;
    font-family: "Righteous", "Trebuchet MS", sans-serif;
    font-size: 31px;
    line-height: 50px;
    letter-spacing: 1px;
    text-transform: uppercase;
    color: var(--ink);
  }
  .flyer__illustration {
    position: absolute;
    left: 90px;
    top: 255px;
    width: 310px;
    height: 220px;
    border-radius: 6px;
    background: linear-gradient(135deg, #f1f1f1 0%, #d9d9da 100%);
  }
  .flyer__business {
    position: absolute;
    top: 478px;
    width: 100%;
    text-align: center;
    font-family: "Open Sans", Arial, sans-serif;
    font-weight: 700;
    font-size: 18.5px;
    letter-spacing: 0.2px;
    text-transform: uppercase;
    color: var(--ink);
  }
  .flyer__phone-band {
    position: absolute;
    top: 523px;
    left: 0;
    width: 100%;
    height: 75px;
    background: var(--band);
    display: flex;
    align-items: center;
    justify-content: center;
    gap: 14px;
    color: var(--band-text);
  }
  .flyer__phone-icon { width: 32px; height: 40px; fill: var(--band-text); }
  .flyer__phone-number {
    font-family: "Open Sans", Arial, sans-serif;
    font-weight: 700;
    font-size: 44px;
    letter-spacing: 0.5px;
  }
  .flyer__email {
    position: absolute;
    top: 617px;
    width: 100%;
    display: flex;
    align-items: center;
    justify-content: center;
    gap: 10px;
    font-family: "Open Sans", Arial, sans-serif;
    font-size: 17px;
    color: var(--ink);
  }
  .flyer__email-icon {
    width: 22px; height: 16px;
    fill: none; stroke: var(--ink); stroke-width: 1.6;
  }
</style>
</head>
<body>
<main class="canvas">
  <section class="flyer">
    <h1 class="flyer__headline">
      At your home,<br>
      On your computer,<br>
      Answering your<br>
      questions
    </h1>

    <div class="flyer__illustration" role="img"
         aria-label="Grey silhouette illustration of a woman seated at a desk with a laptop, surrounded by question marks"></div>

    <p class="flyer__business">Derek Halloway Computer Services</p>

    <div class="flyer__phone-band">
      <svg class="flyer__phone-icon" viewBox="0 0 32 40" aria-hidden="true">
        <path d="M9 2c1.5-.8 3 0 3.6 1.4l2.2 6c.5 1.3 0 2.6-1.1 3.3l-2.3 1.4c-.6.4-.8 1.1-.6 1.8 1.2 4 3 7.4 5.4 10.4.4.5 1.2.7 1.8.4l2.4-1.2c1.2-.6 2.6-.3 3.4.8l3.9 5c.9 1.2.6 2.9-.7 3.7l-2.8 1.8c-2 1.3-4.6 1.3-6.6-.1C10.1 32 4.8 22.7 3.9 12.2c-.2-2.4 1-4.7 3-6z"/>
      </svg>
      <span class="flyer__phone-number">0412-583-906</span>
    </div>

    <p class="flyer__email">
      <svg class="flyer__email-icon" viewBox="0 0 22 16" aria-hidden="true">
        <rect x="1" y="1" width="20" height="14"/>
        <path d="M1 1l10 8 10-8M1 15l7-6M21 15l-7-6"/>
      </svg>
      <span>dhalloway.pcservices@brindlemail.example</span>
    </p>
  </section>
</main>
</body>
</html>
```